I'm a family owned and operated electrical contractor in Colorado USA. We offer a full electrical service, remodel and new construction, we also offer energy saving solutions like LED lighting, photo voltaic, and wind energy,
We sell and install BrightNova light fixtures (rbightNova.com)
More information about my business can be looked at my website copperpeakelcetric.com My logo is on my website.

Industry/Entity Type

Electrical

Contact Information for Business Card

Copper Peak Electric, Dwight Sorensby, Owner, BrightNova Sale & Install, Full Electrical Service, Remodel & New Construction. P: 303-512-8847 F:303-264-3318 E:dwight@copperpeakelectric.com, 27519 CR41, Ridgehollow, CO 80194

```html
<!DOCTYPE html>
<html lang="en">
<head>
<meta charset="utf-8">
<title>Copper Peak Electric – Business Card</title>
<link rel="stylesheet" href="https://fonts.googleapis.com/css2?family=Jost:wght@400;500;600;700&display=swap">
<style>
  :root {
    --page-bg: #e6e7e8;
    --card-top: #ffffff;
    --card-bottom: #eceeef;
    --green-light: #8fd85a;
    --green: #5cbf2a;
    --green-dark: #3f9a1a;
    --ink: #1f1f1f;
    --ink-soft: #333333;
    --white: #ffffff;
  }
  * { box-sizing: border-box; margin: 0; padding: 0; }
  html, body { width: 1200px; height: 800px; overflow: hidden; }
  body {
    background: var(--page-bg);
    font-family: "Jost", sans-serif;
    display: flex;
    align-items: center;
    justify-content: center;
    gap: 40px;
  }
  .card {
    width: 540px;
    height: 309px;
    background: linear-gradient(160deg, var(--card-top), var(--card-bottom));
    box-shadow: 0 2px 10px rgba(0,0,0,0.15);
    position: relative;
  }

  /* Front */
  .card-front {
    display: flex;
    flex-direction: column;
    align-items: center;
    padding-top: 34px;
  }
  .company-name {
    font-weight: 700;
    font-size: 21px;
    letter-spacing: 0.3px;
    color: var(--ink);
    text-transform: uppercase;
  }
  .service-icons {
    display: flex;
    gap: 12px;
    margin-top: 14px;
  }
  .service-icon {
    width: 42px;
    height: 42px;
    border-radius: 50%;
    background: radial-gradient(circle at 40% 30%, var(--green-light), var(--green) 55%, var(--green-dark));
    box-shadow: 0 1px 2px rgba(0,0,0,0.25);
  }
  .name-bar {
    margin-top: 28px;
    background: linear-gradient(180deg, var(--green-light), var(--green) 60%, var(--green-dark));
    color: var(--white);
    padding: 4px 12px 5px;
    border: 1px solid var(--green-dark);
    display: flex;
    align-items: baseline;
  }
  .person-name { font-size: 28px; font-weight: 500; }
  .person-title { font-size: 16px; font-weight: 400; }
  .services {
    list-style: none;
    text-align: center;
    margin-top: 16px;
    font-size: 15px;
    line-height: 1.35;
    color: var(--ink-soft);
  }

  /* Back */
  .card-back {
    display: flex;
    align-items: center;
    justify-content: center;
  }
  .contact-list {
    list-style: none;
    display: flex;
    flex-direction: column;
    gap: 5px;
    width: 360px;
  }
  .contact-row {
    display: flex;
    align-items: center;
    gap: 10px;
    height: 34px;
    padding: 0 14px;
    background: linear-gradient(180deg, var(--green-light), var(--green) 60%, var(--green-dark));
    border: 1px solid var(--green-dark);
    color: var(--white);
    font-size: 15px;
    white-space: nowrap;
  }
  .contact-row svg { width: 16px; height: 16px; flex: none; }
</style>
</head>
<body>

<section class="card card-front">
  <h1 class="company-name">Copper Peak Electric</h1>
  <div class="service-icons">
    <span class="service-icon" role="img" aria-label="Solar energy icon"></span>
    <span class="service-icon" role="img" aria-label="Wind energy icon"></span>
    <span class="service-icon" role="img" aria-label="Green growth icon"></span>
    <span class="service-icon" role="img" aria-label="Water drop icon"></span>
  </div>
  <div class="name-bar">
    <span class="person-name">Dwight Sorensby</span><span class="person-title">,owner</span>
  </div>
  <ul class="services">
    <li>BrightNova Sale &amp; Install</li>
    <li>Full Electrical Service</li>
    <li>Remodel &amp; New Construction</li>
  </ul>
</section>

<section class="card card-back">
  <ul class="contact-list">
    <li class="contact-row">
      <svg viewBox="0 0 16 16" aria-hidden="true"><path fill="none" stroke="#fff" stroke-width="1.5" d="M4 1.5l2.2 3-1.4 1.6c.9 2 2.4 3.5 4.4 4.4l1.6-1.4 3 2.2-1.3 2.2C7 13 3 9 2 3z"/></svg>
      303-512-8847
    </li>
    <li class="contact-row">
      <svg viewBox="0 0 16 16" aria-hidden="true"><rect x="4" y="1.5" width="8" height="4" fill="none" stroke="#fff" stroke-width="1.3"/><rect x="1.5" y="5.5" width="13" height="6" fill="#fff"/><rect x="4" y="10" width="8" height="4.5" fill="none" stroke="#fff" stroke-width="1.3"/></svg>
      303-264-3318
    </li>
    <li class="contact-row">
      <svg viewBox="0 0 16 16" aria-hidden="true"><rect x="1.5" y="3.5" width="13" height="9" fill="none" stroke="#fff" stroke-width="1.3"/><path d="M1.5 3.5L8 9l6.5-5.5" fill="none" stroke="#fff" stroke-width="1.3"/></svg>
      dwight@copperpeakelectric.com
    </li>
    <li class="contact-row">
      <svg viewBox="0 0 16 16" aria-hidden="true"><circle cx="8" cy="8" r="6.3" fill="none" stroke="#fff" stroke-width="1.3"/><ellipse cx="8" cy="8" rx="2.8" ry="6.3" fill="none" stroke="#fff" stroke-width="1.1"/><path d="M1.7 8h12.6" stroke="#fff" stroke-width="1.1"/></svg>
      www.copperpeakelcetric.com
    </li>
    <li class="contact-row">
      <svg viewBox="0 0 16 16" aria-hidden="true"><path d="M8 15s5-5.2 5-8.5A5 5 0 0 0 3 6.5C3 9.8 8 15 8 15z" fill="none" stroke="#fff" stroke-width="1.3"/><circle cx="8" cy="6.5" r="1.8" fill="#fff"/></svg>
      27519 CR41, Ridgehollow, CO 80194
    </li>
  </ul>
</section>

</body>
</html>
```